Brindle 48 Focus Wheel

We need a professional **framework wheel diagram** designed for our detection dog training manual.

Our business is **Brindle 48 Dog Training**, and this graphic represents our **Detection Training Model**.

Please use the **attached reference images** as a guide for the structure and layout of the wheel.

### What we need

1. **Full wheel graphic**

* Clean circular framework wheel
* Similar structure to the attached example
* Clear sections and text
* Professional training manual style
* Transparent background

2. **Individual segment pieces**

We also need the **inner sections broken into separate pieces** (like the second reference image).

This will allow us to place each section on different pages of the manual when explaining the concepts.

Each piece should look like a **slice of the wheel**.

### Style

The design should look:

• Professional
• Clean and modern
• Structured and easy to read
• Suitable for a training manual

Avoid cartoon styles or clipart.

### Colours

Please use our brand colour palette (see attached image):

* Dark navy blue
* Steel blue
* Light blue
* White
* Light grey
* Dark grey

### Files required

Final files must include:

* Vector files (AI or EPS)
* Transparent PNG
* High-resolution PDF

Please also provide **each segment exported individually**

```html
<!DOCTYPE html>
<html lang="en">
<head>
<meta charset="utf-8">
<title>Inner Sections – Separate Pieces</title>
<link href="https://fonts.googleapis.com/css2?family=Outfit:wght@400&family=Heebo:wght@700&display=swap" rel="stylesheet">
<style>
  :root {
    --navy: #2c4460;
    --steel: #5d9bb6;
    --light-grey: #f5f5f5;
    --ink: #1e1e22;
    --white: #ffffff;
  }
  html, body {
    margin: 0;
    padding: 0;
    background: var(--white);
    overflow: hidden;
  }
  .canvas {
    position: relative;
    width: 1122px;
    height: 1200px;
    overflow: hidden;
    background: var(--white);
  }
  .sheet-title {
    position: absolute;
    top: 120px;
    left: 0;
    width: 1102px;
    margin: 0;
    text-align: center;
    font-family: "Outfit", sans-serif;
    font-weight: 400;
    font-size: 34px;
    line-height: 1.2;
    letter-spacing: 0.3px;
    color: var(--ink);
  }
  .segment-sheet {
    position: absolute;
    top: 0;
    left: 0;
    width: 1122px;
    height: 1200px;
  }
  .slice-core--upper { fill: var(--steel); }
  .slice-rim--upper { fill: var(--light-grey); }
  .slice-core--lower { fill: var(--navy); }
  .slice-rim--lower { fill: var(--steel); }
  .slice-label {
    font-family: "Heebo", sans-serif;
    font-weight: 700;
    font-size: 37px;
    text-anchor: middle;
  }
  .slice-label--upper { fill: var(--navy); }
  .slice-label--lower { fill: var(--steel); }
</style>
</head>
<body>
<div class="canvas">
  <h1 class="sheet-title">inner sections broken into separate pieces</h1>

  <svg class="segment-sheet" viewBox="0 0 1860 1990" xmlns="http://www.w3.org/2000/svg">
    <defs>
      <path id="upper-core" d="M0 0 L-145.2 -447 A470 470 0 0 1 145.2 -447 Z"/>
      <path id="upper-rim" d="M-145.2 -447 L-168.7 -519.3 A546 546 0 0 1 168.7 -519.3 L145.2 -447 A470 470 0 0 0 -145.2 -447 Z"/>
      <path id="lower-core" d="M0 0 L179.9 434.2 A470 470 0 0 1 -179.9 434.2 Z"/>
      <path id="lower-rim" d="M179.9 434.2 L209 504.4 A546 546 0 0 1 -209 504.4 L-179.9 434.2 A470 470 0 0 0 179.9 434.2 Z"/>

      <!-- Label baselines: concentric arcs -->
      <path id="arc-up-342" d="M-219.8 -262 A342 342 0 0 1 219.8 -262"/>
      <path id="arc-up-355" d="M-228.2 -271.9 A355 355 0 0 1 228.2 -271.9"/>
      <path id="arc-up-380" d="M-244.3 -291.1 A380 380 0 0 1 244.3 -291.1"/>
      <path id="arc-up-395" d="M-253.9 -302.6 A395 395 0 0 1 253.9 -302.6"/>
      <path id="arc-up-418" d="M-268.7 -320.2 A418 418 0 0 1 268.7 -320.2"/>
      <path id="arc-up-340" d="M-218.5 -260.5 A340 340 0 0 1 218.5 -260.5"/>
      <path id="arc-low-345" d="M-221.8 264.3 A345 345 0 0 0 221.8 264.3"/>
      <path id="arc-low-365" d="M-234.6 279.6 A365 365 0 0 0 234.6 279.6"/>
      <path id="arc-low-385" d="M-247.5 294.9 A385 385 0 0 0 247.5 294.9"/>
      <path id="arc-low-405" d="M-260.3 310.2 A405 405 0 0 0 260.3 310.2"/>
      <path id="arc-low-425" d="M-273.2 325.6 A425 425 0 0 0 273.2 325.6"/>
    </defs>

    <!-- Upper pieces: foundations -->
    <g class="slice" transform="translate(893 1022) rotate(-72)">
      <use href="#upper-rim" class="slice-rim--upper"/>
      <use href="#upper-core" class="slice-core--upper"/>
      <text class="slice-label slice-label--upper"><textPath href="#arc-up-395" startOffset="50%">Genetic</textPath></text>
      <text class="slice-label slice-label--upper"><textPath href="#arc-up-355" startOffset="50%">Suitability</textPath></text>
    </g>

    <g class="slice" transform="translate(788 860) rotate(-36)">
      <use href="#upper-rim" class="slice-rim--upper"/>
      <use href="#upper-core" class="slice-core--upper"/>
      <text class="slice-label slice-label--upper"><textPath href="#arc-up-418" startOffset="50%">Health &amp;</textPath></text>
      <text class="slice-label slice-label--upper"><textPath href="#arc-up-380" startOffset="50%">Physical</textPath></text>
      <text class="slice-label slice-label--upper"><textPath href="#arc-up-342" startOffset="50%">Wellbeing</textPath></text>
    </g>

    <g class="slice" transform="translate(905 1015)">
      <use href="#upper-rim" class="slice-rim--upper"/>
      <use href="#upper-core" class="slice-core--upper"/>
      <text class="slice-label slice-label--upper"><textPath href="#arc-up-380" startOffset="50%">Engagement</textPath></text>
      <text class="slice-label slice-label--upper"><textPath href="#arc-up-340" startOffset="50%">Relationship</textPath></text>
    </g>

    <g class="slice" transform="translate(1007 870) rotate(36)">
      <use href="#upper-rim" class="slice-rim--upper"/>
      <use href="#upper-core" class="slice-core--upper"/>
      <text class="slice-label slice-label--upper"><textPath href="#arc-up-395" startOffset="50%">Reward</textPath></text>
      <text class="slice-label slice-label--upper"><textPath href="#arc-up-355" startOffset="50%">Value</textPath></text>
    </g>

    <g class="slice" transform="translate(1122 932) rotate(72)">
      <use href="#upper-rim" class="slice-rim--upper"/>
      <use href="#upper-core" class="slice-core--upper"/>
      <text class="slice-label slice-label--upper"><textPath href="#arc-up-395" startOffset="50%">Arousal</textPath></text>
      <text class="slice-label slice-label--upper"><textPath href="#arc-up-355" startOffset="50%">Regulation</textPath></text>
    </g>

    <!-- Lower pieces: handler skills -->
    <g class="slice" transform="translate(913 1030) rotate(-67.5)">
      <use href="#lower-rim" class="slice-rim--lower"/>
      <use href="#lower-core" class="slice-core--lower"/>
      <text class="slice-label slice-label--lower"><textPath href="#arc-low-365" startOffset="50%">Read</textPath></text>
      <text class="slice-label slice-label--lower"><textPath href="#arc-low-405" startOffset="50%">The Dog</textPath></text>
    </g>

    <g class="slice" transform="translate(993 1233) rotate(-22.5)">
      <use href="#lower-rim" class="slice-rim--lower"/>
      <use href="#lower-core" class="slice-core--lower"/>
      <text class="slice-label slice-label--lower"><textPath href="#arc-low-345" startOffset="50%">Mimimal</textPath></text>
      <text class="slice-label slice-label--lower"><textPath href="#arc-low-385" startOffset="50%">Necessary</textPath></text>
      <text class="slice-label slice-label--lower"><textPath href="#arc-low-425" startOffset="50%">Involvement</textPath></text>
    </g>

    <g class="slice" transform="translate(901 1033) rotate(22.5)">
      <use href="#lower-rim" class="slice-rim--lower"/>
      <use href="#lower-core" class="slice-core--lower"/>
      <text class="slice-label slice-label--lower"><textPath href="#arc-low-365" startOffset="50%">Search</textPath></text>
      <text class="slice-label slice-label--lower"><textPath href="#arc-low-405" startOffset="50%">Coverage</textPath></text>
    </g>

    <g class="slice" transform="translate(738 1095) rotate(67.5)">
      <use href="#lower-rim" class="slice-rim--lower"/>
      <use href="#lower-core" class="slice-core--lower"/>
      <text class="slice-label slice-label--lower"><textPath href="#arc-low-365" startOffset="50%">Dog</textPath></text>
      <text class="slice-label slice-label--lower"><textPath href="#arc-low-405" startOffset="50%">Safety</textPath></text>
    </g>
  </svg>
</div>
</body>
</html>
```